Feature film needs look book digital brochure - Media/Investor's package

Looking for a designer to create an edgy, eye popping visual representation of my film to get interest from investors, producers and actors, along with Investor and Sponsorship information. Basically it would introduce the project and in about 9-13 pages; give an overview of the film, why to invest, an artistic statement and potential casting ideas and an introduction to the key crew. I have included images (probably more than you need), our film's key art (iron dusk final image & bib logo), and our company (Morvane)'s logo. I've also included samples for another film (gtkr_proposal.pdf) and a proposal I already did for the film. The sample for the other film is more visual and something I'd like to emulate.

The film is called Iron Dusk: a sports drama about two triathletes who overcome their personal demons to train for and compete in the biggest race of their lives.

```html
<!DOCTYPE html>
<html lang="en">
<head>
<meta charset="utf-8">
<title>Iron Dusk – Proposal Synopsis Spread</title>
<link rel="stylesheet" href="https://fonts.googleapis.com/css2?family=Open+Sans:wght@300;400;600&display=swap">
<style>
  :root {
    --sky-top: #b9c6cc;
    --sky-mid: #dfe3d8;
    --field: #b9b58a;
    --field-deep: #8f9468;
    --track: #9e9788;
    --track-deep: #7d766a;
    --veil: rgba(255, 255, 255, 0.55);
    --accent-blue: #2a97d8;
    --panel-blue: rgba(38, 150, 212, 0.86);
    --ink-dark: #1d2a33;
    --white: #ffffff;
    --fold: #4a4a4a;
  }
  * { margin: 0; padding: 0; box-sizing: border-box; }
  html, body { width: 1200px; height: 849px; overflow: hidden; background: #ffffff; }
  body { font-family: "Open Sans", sans-serif; }

  .spread { position: relative; width: 1200px; height: 849px; overflow: hidden; }

  .backdrop {
    position: absolute; inset: 0;
    background: linear-gradient(180deg,
      var(--sky-top) 0%, var(--sky-mid) 30%, #d6d6bf 42%,
      var(--field) 55%, var(--field-deep) 66%,
      var(--track) 76%, var(--track-deep) 100%);
  }

  .fold {
    position: absolute; left: 597px; top: 0; width: 1px; height: 849px;
    background: var(--fold);
  }

  /* Left page */
  .cover-panel {
    position: absolute; left: 40px; top: 64px; width: 503px; height: 733px;
    background: var(--veil);
  }
  .logline {
    position: absolute; left: 95px; top: 136px; width: 395px;
    text-align: center; color: var(--accent-blue);
    font-weight: 300; font-size: 31px; line-height: 38.5px;
  }
  .race-photo {
    position: absolute; left: 78px; top: 431px; width: 424px; height: 313px;
    background: linear-gradient(180deg, #a9bfd4 0%, #7f95a6 40%, #6a6c6a 62%, #4d4d4f 100%);
  }

  /* Right page */
  .synopsis-panel {
    position: absolute; left: 644px; top: 64px; width: 502px; height: 724px;
    background: var(--panel-blue);
  }
  .proposal-line {
    position: absolute; left: 0; top: 42px; width: 100%;
    text-align: center; color: var(--ink-dark);
    font-size: 15px; font-weight: 400;
  }
  .section-title {
    position: absolute; left: 0; top: 58px; width: 100%;
    text-align: center; color: var(--white);
    font-size: 78px; font-weight: 400; letter-spacing: 1px; line-height: 86px;
  }
  .synopsis-body {
    position: absolute; left: 20px; top: 150px; width: 464px;
    color: var(--white); font-size: 8.25px; line-height: 11.6px; font-weight: 400;
  }
  .synopsis-body p { margin-bottom: 11.6px; }
</style>
</head>
<body>
<main class="spread">
  <div class="backdrop" role="img" aria-label="Hazy sky over green fields above a running track with numbered lanes"></div>
  <div class="fold"></div>

  <section class="cover-panel" aria-label="Logline page"></section>
  <h2 class="logline">Two triathletes battle personal demons while they train for the biggest event of their lives.</h2>
  <div class="race-photo" role="img" aria-label="Cyclists in helmets racing down a road during a triathlon, the leader waving"></div>

  <section class="synopsis-panel">
    <p class="proposal-line">Iron Dusk Proposal- Hollis Reed Grant - June 12, 2014</p>
    <h1 class="section-title">SYNOPSIS</h1>
    <div class="synopsis-body">
      <p>Thousands of swimmers pile over one another, cyclists speed down a hill at 80kph, and runners summon every ounce of their soul to make it to the finish line. This is their story... This is the story of Iron Dusk.</p>
      <p>TREVOR is in the twilight of his semi-professional triathlete career. His girlfriend, CORA, has always been supportive and until recently, used to go to all the events with him and cheer him on. To Trevor, their relationship has become more of a burden and a distraction. After coming second in a big race in Austria, Trevor lashes out at Cora and she dumps him, the culmination of years of emotional abuse. Depressed, rejected, and alone, Cora decides a change is needed. With Cora no longer providing extra financial support, Trevor reluctantly accepts a young rival's request for coaching.</p>
      <p>After facing serious anxiety over a life seemingly wasted, Cora goes on a long evening run, longer than she's ever taken before. She returns home, sweaty and sore, but inspired. She goes on another run, and another and becomes fiercely determined to train every day, dragging LEXI, her best friend, with her to the beach to watch her swim. Lexi thinks Cora is doing this to get back into a relationship with Trevor and does not hide her disapproval. Lexi and Cora have a major falling out and Cora is left to face the challenge of a triathlon without the support of her best friend. Driven by a newly discovered competitive spirit and a new community she's found through running, Cora races a local triathlon and qualifies for the World Championships, the same race her ex-boyfriend is fighting to win. Her training intensifies as she battles her conflicted soul.</p>
      <p>Trevor's become a little distracted by VANESSA, a reporter doing an exposé on him and his year of redemption. During a race, Trevor hits a set back and is unable to continue the race. He explodes with blame, anger, and fury on the course. Meanwhile his biggest competitor, SEBASTIAN KUREK, has just won another major competition. As Trevor opens up to Vanessa like he's never done before to anyone, she ends the relationship; she's just not the right girl for him.</p>
      <p>Trevor the veteran and Cora the new kid on the block - both facing the World Championships alone. Following an interview with the press, Trevor runs into Cora causing all her insecurities and doubts to resurface again. Trevor's guilt over how he treated her impacts his once-unwavering desire to win. During the race, Cora, never having competed in anything so grueling as this, fights off every urge to quit, her instinctual response to adversity in the past. Trevor is faced with another challenge of his own. When an unforeseen accident occurs on the course, Trevor has to decide whether he will explode in blame and anger or to finish what he started.</p>
      <p>They meet at the 13 Mile Aid Station, the halfway mark of the "run" segment of the triathlon. Exhausted and fatigued, they run the last 13 miles together. They cross the line one minute before the finish cut off. The greatest race of their life, completed - not because of a finishing time or a medal, but the personal journey each has traversed to get to this moment, together.</p>
    </div>
  </section>
</main>
</body>
</html>
```